Webdesign für Arbeitsschutz
Zielgruppe
Grundlage für ein funktionierendes Beschäftigungssystem ist die Schaffung und der Erhalt sicherer und menschengerechter Arbeitsbedingungen. Ein effizienter Arbeitsschutz und eine wirksame Unfallvermeidung sind hierfür besonders wichtig, vor allem auch im Hinblick auf die Herausforderungen einer durch digitalen Wandel immer schnelleren und anspruchsvolleren Arbeitswelt. Sicherheit und Gesundheit bei der Arbeit sind deshalb wichtige Arbeitsschwerpunkte im Bundesamt für Wohnbau und Gewässerpflege. Ziel ist es, die Beschäftigten wirksam vor Gefahren und gesundheitlichen Schädigungen zu schützen. Verlässliche gesetzliche Grundlagen und rechtssichere Rahmenbedingungen für alle Unternehmen sind dafür unerlässlich.
Das wichtigste Grundlagengesetz für den betrieblichen Arbeitsschutz ist das Arbeitsschutzgesetz (ArbSchG). Es verpflichtet den Arbeitgeber, Gesundheitsgefährdungen am Arbeitsplatz zu beurteilen und über notwendige Schutzmaßnahmen zu entscheiden. Der Arbeitgeber hat für eine funktionierende Arbeitsschutzorganisation im Betrieb zu sorgen. Dies kann besonders wirksam durch eine nachhaltige Einbindung des Arbeits- und Gesundheitsschutzes in die Strukturen und Abläufe eines Unternehmens erreicht werden.
Aufgabenstellung
Gerne eine helle Seite mit schöner integration des Logo´s in die Homepage
Ich möchte keine exakte Kopie der Internet-Seite haben, aber alle Inhalte die Velm-Arbeitsschutz anbietet (inkl. Rückrufservice, Anbringen von Referenz-Logos, Navigationsmenü)
Die Gestaltung der Hauptseite mit Farbe sollte bitte mit den vorhandenen Logo harmonieren. Die Aufteilung wo sich die Bausteine (Rückrufservice etc.) befindet sollte übersichtlich angebracht sein.

```html
<!DOCTYPE html>
<html lang="de">
<head>
<meta charset="utf-8">
<title>Velm Arbeitsschutz – Startseite</title>
<link href="https://fonts.googleapis.com/css2?family=Poppins:wght@300;400;500;600;700&display=swap" rel="stylesheet">
<style>
:root{
  --teal:#2e6a80;
  --teal-dark:#24586b;
  --ink:#333b40;
  --muted:#666d72;
  --line:#dde2e5;
  --soft:#f6f7f8;
  --white:#ffffff;
}
*{margin:0;padding:0;box-sizing:border-box}
html,body{width:1200px;height:3388px;overflow:hidden;background:var(--white)}
body{font-family:'Poppins',sans-serif;color:var(--ink)}
.page{position:relative;width:1200px;height:3388px;overflow:hidden}
.abs{position:absolute}
a{color:inherit;text-decoration:none}

/* hero */
.hero{left:0;top:0;width:1200px;height:707px;
  background:linear-gradient(100deg,#f1f3f4 0%,#e9edf0 35%,#d9dfe4 55%,#c2ccd6 75%,#cfd6de 100%)}
.brand{left:0;top:26px;width:1200px;text-align:center;color:var(--teal)}
.brand .mark{display:inline-block;width:14px;height:14px;background:var(--teal);margin-bottom:8px}
.brand .name{font-size:10px;line-height:13px}
.contact-icons{left:1098px;top:56px;display:flex;gap:10px}
.nav{left:62px;top:118px;width:1076px;height:50px;border-top:1px solid var(--line);border-bottom:1px solid var(--line);
  display:flex;justify-content:center;align-items:center;gap:19px;font-size:13px;color:var(--ink)}
.nav .active{color:var(--teal)}
.hero-band{left:0;top:307px;width:505px;height:225px}
.hero-title{left:62px;top:348px;color:var(--white);font-size:37px;line-height:42px;font-weight:300}
.hero-title strong{font-weight:600;display:block}
.btn-outline{left:62px;top:450px;width:156px;height:37px;border:2px solid var(--white);color:var(--white);
  font-size:13px;display:flex;align-items:center;justify-content:center}

/* section heading */
.sec-head{left:0;width:1200px;display:flex;justify-content:center;align-items:flex-end;gap:14px}
.sec-head h2{font-size:18px;font-weight:500;letter-spacing:.3px}
.sec-head .slash{width:14px;height:24px;border-right:2px solid var(--teal);transform:skewX(-25deg);margin-bottom:-6px}
.sec-head span{font-size:12px;color:var(--muted);margin-bottom:-8px}

/* services */
.svc{width:300px}
.svc h3{font-size:14px;font-weight:500;margin-bottom:14px}
.svc p{font-size:10.5px;line-height:17px;color:var(--muted)}
.svc a{display:block;font-size:10px;font-weight:600;color:var(--teal);margin-top:12px}
.svc.left{text-align:right}
.svc-icon{width:56px;height:50px}
.center-name{left:500px;top:1058px;width:200px;text-align:center;color:var(--teal)}
.center-name .sq{display:inline-block;width:60px;height:60px;background:var(--teal);margin-bottom:18px}
.center-name p{font-size:11.5px;line-height:19px;font-weight:500}

/* about */
.about{left:0;top:1401px;width:1200px;height:714px;background:var(--soft)}
.about-lead{left:0;top:1538px;width:1200px;text-align:center;color:var(--teal);font-size:13px;line-height:21px}
.card-title{width:300px;text-align:center;font-size:19px;font-weight:500;line-height:22px}
.card{width:300px;background:var(--white);text-align:center;padding:30px 34px 0}
.card p{font-size:10px;line-height:18px;color:var(--muted)}
.btn-fill{display:inline-flex;width:122px;height:28px;background:var(--teal);color:var(--white);font-size:11px;font-weight:500;
  align-items:center;justify-content:center;margin-top:26px}

/* callback */
.callback{left:0;top:2115px;width:1200px;height:560px;
  background:linear-gradient(90deg,#4d4f52 0%,#6e6c6a 45%,#87817b 70%,#5f6062 100%)}
.callback-title{left:480px;top:2195px;color:var(--white);font-size:25px;font-weight:500}
.field{color:var(--white);font-size:12px;border-bottom:1px solid rgba(255,255,255,.75);height:22px;display:flex;justify-content:space-between;align-items:flex-start}
.field.small{font-size:10.5px;height:18px}
.btn-white{left:671px;top:2540px;width:154px;height:37px;background:var(--white);color:var(--teal);font-size:15px;font-weight:600;
  display:flex;align-items:center;justify-content:center}

/* references */
.ref{top:2845px;height:40px;display:flex;align-items:center;justify-content:center;font-weight:600;font-size:15px;color:var(--ink)}

/* footer */
.footer{left:0;top:2977px;width:1200px;height:375px;background:#f4f5f6}
.f-title{color:var(--teal);font-size:18px;font-weight:600;line-height:30px}
.f-line{display:flex;align-items:center;gap:12px;font-size:12.5px;color:var(--muted);height:25px}
.f-list li{list-style:none;display:flex;align-items:center;gap:14px;font-size:12.5px;color:var(--muted);height:25px}
.f-list li::before{content:"";width:10px;height:10px;background:var(--ink)}
.f-brand{left:400px;top:3148px;width:400px;text-align:center;color:var(--teal);font-size:17px;line-height:23px}
.f-brand .sq{display:inline-block;width:50px;height:50px;background:var(--teal);margin-bottom:18px}
.copy{left:0;top:3352px;width:1200px;height:36px;background:var(--teal);color:var(--white);font-size:12.5px;font-weight:500;
  display:flex;align-items:center;justify-content:center}
</style>
</head>
<body>
<div class="page">

  <!-- hero -->
  <div class="abs hero" role="img" aria-label="Foto: Handwerker im karierten Hemd hält einen orangefarbenen Schutzhelm vor einer Baustelle mit Kran"></div>

  <div class="abs brand">
    <span class="mark"></span>
    <div class="name">Arbeitssicherheit &amp; Gesundheitsschutz<br>Süd GmbH</div>
  </div>
  <div class="abs contact-icons">
    <svg width="13" height="12" viewBox="0 0 13 12"><rect x="0" y="2" width="13" height="9" fill="#2e6a80"/><path d="M0 2 L6.5 7 L13 2" stroke="#fff" stroke-width="1.2" fill="none"/></svg>
    <svg width="13" height="13" viewBox="0 0 24 24"><path fill="#2e6a80" d="M6.6 10.8a15.1 15.1 0 006.6 6.6l2.2-2.2c.3-.3.7-.4 1-.2 1.1.4 2.3.6 3.6.6.6 0 1 .4 1 1V20c0 .6-.4 1-1 1A17 17 0 013 4c0-.6.4-1 1-1h3.5c.6 0 1 .4 1 1 0 1.3.2 2.5.6 3.6.1.3 0 .7-.2 1z"/></svg>
  </div>
  <nav class="abs nav">
    <a class="active">Startseite</a><a>Beratung &amp; Betreuung</a><a>Seminare</a><a>E-Learning</a><a>Beauftragtenwesen</a><a>Das Unternehmen</a><a>Kontakt</a>
  </nav>

  <svg class="abs hero-band" viewBox="0 0 505 225"><polygon points="0,0 505,0 358,225 0,225" fill="#2e6a80" fill-opacity=".88"/></svg>
  <h1 class="abs hero-title">Mit Sicherheit Mehr<strong>Sicherheit</strong></h1>
  <a class="abs btn-outline">Mehr anzeigen</a>

  <!-- services -->
  <div class="abs sec-head" style="top:762px"><h2>DIENSTLEISTUNGEN</h2><i class="slash"></i><span>Sie wissen, was wir anbieten</span></div>

  <div class="abs svc left" style="left:68px;top:882px">
    <h3>Wir stellen ein</h3>
    <p>Informieren Sie sich über<br>unsere Stellenangebote.</p>
    <a>zu den Stellenausschreibungen</a>
  </div>
  <svg class="abs svc-icon" style="left:388px;top:876px" viewBox="0 0 56 50" fill="none" stroke="#2e6a80" stroke-width="3"><circle cx="22" cy="15" r="10"/><path d="M4 46c0-10 8-17 18-17s18 7 18 17z"/><path d="M46 10v14M39 17h14"/></svg>

  <div class="abs svc left" style="left:68px;top:1052px">
    <h3>Arbeitsschutz</h3>
    <p>Sicherheit geht vor! Wir betreuen Ihr<br>Unternehmen als externe Fachkraft für<br>Arbeitssicherheit.</p>
    <a>mehr zum Arbeitsschutz</a>
  </div>
  <svg class="abs svc-icon" style="left:386px;top:1054px" viewBox="0 0 56 50" fill="none" stroke="#2e6a80" stroke-width="3"><path d="M28 3l16 6v14c0 11-7 19-16 23-9-4-16-12-16-23V9z"/><path d="M21 24l5 5 10-10"/></svg>

  <div class="abs svc left" style="left:68px;top:1231px">
    <h3>Seminare</h3>
    <p>Wir bieten eine Vielzahl von fachspe-<br>zifischen Seminaren rund um den<br>Arbeitsschutz.</p>
    <a>Übersicht unserer Seminare</a>
  </div>
  <svg class="abs svc-icon" style="left:388px;top:1224px" viewBox="0 0 56 50" fill="#2e6a80"><circle cx="10" cy="7" r="5"/><rect x="4" y="14" width="12" height="18"/><rect x="5" y="32" width="4" height="16"/><rect x="11" y="32" width="4" height="16"/><rect x="20" y="6" width="32" height="22" fill="none" stroke="#2e6a80" stroke-width="2.5"/><path d="M36 28v8M36 36l-8 12M36 36l8 12" stroke="#2e6a80" stroke-width="2.5"/><path d="M16 18l10-6" stroke="#2e6a80" stroke-width="2.5"/></svg>

  <div class="abs center-name">
    <span class="sq"></span>
    <p>Ihr Ingenieur- und Sachver-<br>ständigenbüro für Arbeitssi-<br>cherheit</p>
  </div>

  <svg class="abs svc-icon" style="left:752px;top:876px" viewBox="0 0 56 50" fill="none" stroke="#2e6a80" stroke-width="3"><rect x="8" y="6" width="40" height="27" rx="2"/><path d="M2 38h52l-3 5H5z" fill="#2e6a80"/></svg>
  <div class="abs svc" style="left:833px;top:882px">
    <h3>E-Learning</h3>
    <p>Sicherheitsunterweisungen online<br>mit E-Learning – flexibel,unkompliziert<br>und zeitsparend.</p>
    <a>alles zum Thema E-Learning</a>
  </div>

  <svg class="abs svc-icon" style="left:770px;top:1050px" viewBox="0 0 56 50" fill="#2e6a80"><rect x="14" y="4" width="4" height="18" rx="2"/><rect x="19" y="1" width="4" height="20" rx="2"/><rect x="24" y="2" width="4" height="19" rx="2"/><rect x="29" y="5" width="4" height="17" rx="2"/><path d="M13 18h21v12c0 7-5 13-11 13s-10-5-10-11z"/><path d="M8 22l6 6" stroke="#2e6a80" stroke-width="4"/></svg>
  <div class="abs svc" style="left:833px;top:1052px">
    <h3>Beauftragtenwesen</h3>
    <p>Übernahme der Beauftragten Funkt-<br>ionen – von Gefahrstoffen bis hin<br>zum Brandschutz.</p>
    <a>mehr zum Beauftragtenwesen</a>
  </div>

  <svg class="abs svc-icon" style="left:756px;top:1228px" viewBox="0 0 56 50" fill="none" stroke="#2e6a80" stroke-width="3"><rect x="12" y="3" width="40" height="30" rx="2"/><path d="M12 10h40"/><rect x="3" y="24" width="6" height="20" fill="#2e6a80"/><path d="M9 30h14c3 0 3 5 0 5h-8M9 42h18l12-8"/></svg>
  <div class="abs svc" style="left:833px;top:1231px">
    <h3>StoffPilot – Gefahrstoff Softwarelösung</h3>
    <p>Gefahrstoff-Management, einfach wie<br>nie zuvor! Flexibel und anpas-sbar<br>an Ihre Prozesse.</p>
    <a>mehr zu StoffPilot</a>
  </div>

  <!-- about -->
  <div class="abs about"></div>
  <div class="abs sec-head" style="top:1483px"><h2>ÜBER UNS</h2><i class="slash"></i><span>unsere Arbeit</span></div>
  <p class="abs about-lead">Ihr Ingenieur- und Sachverständigenbüro für<br>Arbeitssicherheit</p>
  <svg class="abs" style="left:576px;top:1620px" width="48" height="58" viewBox="0 0 48 58" fill="none" stroke="#2e6a80" stroke-width="4"><path d="M24 3l19 7v17c0 14-8 23-19 28C13 50 5 41 5 27V10z"/><path d="M14 28l7 7 13-13"/></svg>

  <svg class="abs" style="left:182px;top:1688px" width="62" height="46" viewBox="0 0 62 46" fill="#2e6a80"><path d="M4 34C4 16 16 2 33 2c14 0 25 10 25 24v6H20c-6 0-10 4-16 8z"/><path d="M2 40c6-4 12-6 20-6h38" stroke="#2e6a80" stroke-width="4" fill="none"/></svg>
  <div class="abs card-title" style="left:62px;top:1753px">Velm<br>Arbeitsschutz</div>
  <div class="abs card" style="left:62px;top:1820px;height:200px">
    <p>Velm Arbeitsschutz ist Ihr zertifizierter Dienstleister für den Raum Karlsruhe und die Region Rhein-Neckar, wenn es um die betriebliche Sicherheit geht.Wir bieten unseren Kunden als externe</p>
    <a class="btn-fill">Lesen Sie mehr</a>
  </div>

  <div class="abs card-title" style="left:450px;top:1690px">Ihre Sicherheit Ist Unsere<br>Aufgabe!</div>
  <div class="abs card" style="left:450px;top:1757px;height:200px">
    <p>Die Implementierung des Arbeits- und Gesundheitsschutzes ist für alle Betriebe egal in welcher Größe und Branche ein wichtiges Thema, denn der Gesetzgeber verpflichtet Unternehmen zur Umsetzung der</p>
    <a class="btn-fill">Lesen Sie mehr</a>
  </div>

  <svg class="abs" style="left:966px;top:1688px" width="44" height="46" viewBox="0 0 44 46" fill="#2e6a80"><circle cx="18" cy="10" r="9"/><path d="M2 44c0-13 7-22 16-22 4 0 7 1 9 3v19z"/><path d="M32 24l10 4v8c0 5-4 8-10 10-6-2-10-5-10-10v-8z"/><path d="M16 22l2 12 2-12" fill="#fff"/></svg>
  <div class="abs card-title" style="left:838px;top:1753px">Fachkraft für<br>Arbeitssicherheit</div>
  <div class="abs card" style="left:838px;top:1820px;height:200px">
    <p>Wir unterstützen Sie als Fachkraft für Arbeitssicherheit bei der Erstellung der Gefährdungsbeurteilung, den regelmäßigen Betriebsbegehungen sowie bei den jährlichen Sicherheitsunterweisungen</p>
    <a class="btn-fill">Lesen Sie mehr</a>
  </div>

  <!-- callback -->
  <div class="abs callback" role="img" aria-label="Foto: Team im Kundenservice mit Headsets, grau abgedunkelt"></div>
  <h2 class="abs callback-title">Unser Rückrufservice</h2>

  <div class="abs field" style="left:480px;top:2296px;width:157px">Anrede* <svg width="10" height="8" viewBox="0 0 10 8"><path d="M1 2l4 4 4-4" stroke="#fff" stroke-width="1.6" fill="none"/></svg></div>
  <div class="abs field" style="left:671px;top:2296px;width:157px">Name *</div>
  <div class="abs field" style="left:862px;top:2296px;width:157px">Vorname *</div>
  <div class="abs field" style="left:480px;top:2356px;width:275px">Firma *</div>
  <div class="abs field" style="left:792px;top:2356px;width:227px"><span style="padding-left:70px">Telefonr. *</span></div>
  <div class="abs field" style="left:480px;top:2410px;width:539px">Betreff *</div>
  <div class="abs field small" style="left:480px;top:2474px;width:157px">Wochentag: <svg width="10" height="8" viewBox="0 0 10 8"><path d="M1 2l4 4 4-4" stroke="#fff" stroke-width="1.6" fill="none"/></svg></div>
  <div class="abs field small" style="left:673px;top:2474px;width:155px">Wochentag: <svg width="10" height="8" viewBox="0 0 10 8"><path d="M1 2l4 4 4-4" stroke="#fff" stroke-width="1.6" fill="none"/></svg></div>
  <div class="abs field small" style="left:862px;top:2474px;width:157px">Wochentag: <svg width="10" height="8" viewBox="0 0 10 8"><path d="M1 2l4 4 4-4" stroke="#fff" stroke-width="1.6" fill="none"/></svg></div>
  <a class="abs btn-white">absenden</a>

  <!-- references -->
  <div class="abs sec-head" style="top:2752px"><h2>AUSZUG AUS UNSEREN REFERENZEN</h2><i class="slash"></i><span>die besten Dienstleistungen</span></div>
  <div class="abs ref" style="left:340px;width:110px">Sonnkap</div>
  <div class="abs ref" style="left:480px;width:100px">Wendrax</div>
  <div class="abs ref" style="left:615px;width:105px">Feloro</div>
  <div class="abs ref" style="left:745px;width:120px">Trallon Logistik</div>

  <!-- footer -->
  <div class="abs footer"></div>
  <div class="abs f-title" style="left:63px;top:3030px">Zögern Sie nicht, kontaktieren<br>Sie uns.</div>
  <div class="abs" style="left:63px;top:3108px">
    <div class="f-line"><svg width="13" height="13" viewBox="0 0 24 24"><path fill="#333b40" d="M6.6 10.8a15.1 15.1 0 006.6 6.6l2.2-2.2c.3-.3.7-.4 1-.2 1.1.4 2.3.6 3.6.6.6 0 1 .4 1 1V20c0 .6-.4 1-1 1A17 17 0 013 4c0-.6.4-1 1-1h3.5c.6 0 1 .4 1 1 0 1.3.2 2.5.6 3.6.1.3 0 .7-.2 1z"/></svg>+49 7000 51620 - 0</div>
    <div class="f-line"><svg width="13" height="13" viewBox="0 0 24 24"><path fill="#333b40" d="M6.6 10.8a15.1 15.1 0 006.6 6.6l2.2-2.2c.3-.3.7-.4 1-.2 1.1.4 2.3.6 3.6.6.6 0 1 .4 1 1V20c0 .6-.4 1-1 1A17 17 0 013 4c0-.6.4-1 1-1h3.5c.6 0 1 .4 1 1 0 1.3.2 2.5.6 3.6.1.3 0 .7-.2 1z"/></svg>+49 7000 51620 - 19</div>
    <div class="f-line"><svg width="13" height="11" viewBox="0 0 13 11"><rect x="0" y="1" width="13" height="9" fill="#333b40"/><path d="M0 1 L6.5 6 L13 1" stroke="#fff" stroke-width="1.2" fill="none"/></svg>info(at)velm-arbeitsschutz.de</div>
    <div class="f-line"><svg width="13" height="13" viewBox="0 0 14 14" fill="none" stroke="#333b40" stroke-width="1.2"><circle cx="7" cy="7" r="6"/><ellipse cx="7" cy="7" rx="2.5" ry="6"/><path d="M1 7h12"/></svg>www.velm-arbeitsschutz.de</div>
  </div>
  <div class="abs" style="left:63px;top:3240px">
    <div class="f-line" style="color:var(--ink);font-weight:600;font-size:11.5px"><svg width="11" height="14" viewBox="0 0 12 16"><path fill="#333b40" d="M6 0a6 6 0 00-6 6c0 4.5 6 10 6 10s6-5.5 6-10a6 6 0 00-6-6zm0 8.5A2.5 2.5 0 116 3.5a2.5 2.5 0 010 5z"/></svg>VELM ARBEITSSCHUTZ GMBH &amp; CO. KG</div>
    <div class="f-line" style="padding-left:21px">Lindenweg 14</div>
    <div class="f-line" style="padding-left:21px">68999 Talheim</div>
  </div>

  <div class="abs f-brand">
    <span class="sq"></span>
    <div>Arbeitssicherheit &amp; Gesundheitsschutz<br>Süd GmbH</div>
  </div>

  <div class="abs f-title" style="left:932px;top:3030px">Software</div>
  <ul class="abs f-list" style="left:932px;top:3076px">
    <li>E-Learning</li>
    <li>Gefahrstoff-Software StoffPilot</li>
  </ul>
  <div class="abs f-title" style="left:938px;top:3158px">Software</div>
  <ul class="abs f-list" style="left:938px;top:3204px">
    <li>Impressum</li>
    <li>Datenschutz</li>
    <li>Netzwerk</li>
    <li>Jobs</li>
  </ul>

  <div class="abs copy">Copyright 2015 <span style="font-weight:400;margin-left:5px">www.velm-arbeitsschutz.de</span></div>
</div>
</body>
</html>
```